Children friendly theme required for simple Maths mobile app

Simply the app presents 100 random maths questions one-by-one that the child attempts to answer within a set time.

The title of the app is "Tally Quest Zoom"

See attached mock-up for further details.

Design elements required:

1. Color scheme: Reasonably colorful.

2. Logo: A stylized clock (with a single sweeping (blurred) hand or “alarm clock” style) with the plus, minus, divide and multiplication symbols and numbers spinning around it. The clock is the largest element with the operator symbols smaller and the number small again (numbers can be a mix of sizes). Logo should have square dimensions and needs to scale as large as 512px square and as small as 29px square. No words should be on the icon.

3. Background: All screens will have a common background containing all or parts of the logo in various sizes and positions. If time permits each screen can have a subtle variation of design (e.g.: slight color change etc).

4. Button with simple down-state. In the mock-up navigation buttons have greater-than/less-than symbols to imply direction/flow. This could instead be included in the button design (e.g.: button outline points more to the left or right). “For Parents” IS a button and will be rendered as text only.

5. Splash screen: Can just contain the title, logo and background.

6. Font: The app uses static and dynamic text so the font(s) used will need to be embedded in the app. I was considering using Comic Sans for the text (including the number keypad).

7. Graphics: The app uses two icons - a “star” and “clock” images/icons to indicate the top score and time-limit respectively for participants. The clock icon probably needs to be the same as the clock image in the logo (although this is not essential).

Important: Design needs to be children friendly but plain as visuals are not the focus.

Screen size will be 320 x 480, portrait only.

Files need to be submitted in 32-bit PNG format.

This is my first time using PixelBazaar and my first time formally specifying a design so please ask questions if anything is unclear.
Updates

Hi all,

Budget has been doubled based on advice from PixelBazaar and feedback from some potential designers.

Regards,
   Gareth

Hi all,

Sorry about a late change in the brief - the title of the app is now "Tally Quest Zoom".

Kind regards,
   Gareth

Target Market(s)

Parent/Teachers (but for children to use) – i.e.: This app will unlikely be discovered/downloaded by children.

Requirements
Nice to have
• Slightly different background for each screen. Screens are numbered 1 to 6 in the mockup.
Should not have
• "Overwhelming" or overpowering visuals. The task/content is the focus.

```html
<!DOCTYPE html>
<html lang="en">
<head>
<meta charset="utf-8">
<title>Tally Quest Zoom – Result</title>
<link href="https://fonts.googleapis.com/css2?family=Comic+Neue:wght@700&display=swap" rel="stylesheet">
<style>
  :root {
    --sky-top: #5fcbf6;
    --sky-bottom: #1688c9;
    --glow: rgba(255, 255, 255, 0.08);
    --panel: rgba(225, 243, 251, 0.78);
    --ink: #1b9ad8;
    --white: #ffffff;
  }
  * { margin: 0; padding: 0; box-sizing: border-box; }
  html, body { width: 800px; height: 1200px; overflow: hidden; }
  body {
    font-family: "Comic Neue", "Comic Sans MS", cursive;
    font-weight: 700;
  }
  .screen {
    position: relative;
    width: 800px;
    height: 1200px;
    overflow: hidden;
    background: linear-gradient(180deg, var(--sky-top) 0%, #3fb0e8 45%, var(--sky-bottom) 100%);
  }
  .backdrop-ring {
    position: absolute;
    left: 170px;
    top: -520px;
    width: 1350px;
    height: 1350px;
    border-radius: 50%;
    background: var(--glow);
  }
  .app-title {
    position: absolute;
    top: 100px;
    left: 0;
    width: 100%;
    text-align: center;
    color: var(--white);
    font-size: 76px;
    line-height: 88px;
    letter-spacing: 1px;
  }
  .result-card {
    position: absolute;
    left: 122px;
    top: 357px;
    width: 545px;
    height: 585px;
    background: var(--panel);
    border-radius: 10px;
    color: var(--ink);
    text-align: center;
  }
  .greeting { position: absolute; top: 52px; width: 100%; font-size: 44px; }
  .score-label { position: absolute; top: 150px; width: 100%; font-size: 44px; }
  .score-value { position: absolute; top: 228px; width: 100%; font-size: 58px; }
  .star-rating { position: absolute; top: 298px; left: 0; width: 100%; display: flex; justify-content: center; }
  .score-detail {
    position: absolute;
    top: 390px;
    width: 100%;
    font-size: 42px;
    line-height: 49px;
  }
  .nav-bar {
    position: absolute;
    top: 1035px;
    left: 0;
    width: 100%;
    height: 70px;
    color: var(--white);
    font-size: 36px;
  }
  .nav-button {
    position: absolute;
    top: 0;
    height: 70px;
    display: flex;
    align-items: center;
    gap: 14px;
  }
  .nav-back { left: 140px; }
  .nav-retry { left: 478px; }
  .timer-icon { position: absolute; left: 350px; top: 0; }
</style>
</head>
<body>
<main class="screen">
  <div class="backdrop-ring"></div>

  <h1 class="app-title">Tally Quest<br>Zoom</h1>

  <section class="result-card">
    <p class="greeting">Well done Rowan!</p>
    <p class="score-label">You got</p>
    <p class="score-value">80</p>
    <svg class="star-rating" width="800" height="64" viewBox="0 0 280 64" aria-label="3.5 stars">
      <defs>
        <symbol id="star" viewBox="-32 -32 64 64">
          <polygon points="0,-28 8,-9 28,-9 12,4 18,25 0,13 -18,25 -12,4 -28,-9 -8,-9"
                   fill="#2aa6e2" stroke="#ffffff" stroke-width="5" stroke-linejoin="round"/>
        </symbol>
        <clipPath id="half"><rect x="210" y="0" width="30" height="64"/></clipPath>
      </defs>
      <use href="#star" x="8" y="2" width="60" height="60"/>
      <use href="#star" x="76" y="2" width="60" height="60"/>
      <use href="#star" x="144" y="2" width="60" height="60"/>
      <use href="#star" x="212" y="2" width="60" height="60" clip-path="url(#half)"/>
    </svg>
    <p class="score-detail">Correct out of 50<br>in 6 minutes and 11<br>seconds</p>
  </section>

  <nav class="nav-bar">
    <div class="nav-button nav-back">
      <svg width="24" height="34" viewBox="0 0 24 34"><polygon points="22,2 2,17 22,32" fill="#63c6f3"/></svg>
      <span>Next</span>
    </div>
    <svg class="timer-icon" width="76" height="76" viewBox="0 0 76 76" aria-label="Timer">
      <circle cx="38" cy="35" r="31" fill="none" stroke="#ffffff" stroke-width="5"/>
      <line x1="38" y1="35" x2="26" y2="20" stroke="#ffffff" stroke-width="4" stroke-linecap="round"/>
    </svg>
    <div class="nav-button nav-retry">
      <span>Try Again</span>
      <svg width="24" height="34" viewBox="0 0 24 34"><polygon points="2,2 22,17 2,32" fill="#63c6f3"/></svg>
    </div>
  </nav>
</main>
</body>
</html>
```